Adventure Business Cards

Please check out our website for style
Vertical card
Details:
Side 1
Logo
Business name: Kestrel Point Wildland Tours
Name: Colin Warbeck
Role: Director
Email: info@kestrelpointtours.com
Address: PO Box 71, Marlin Cove NSW 2471
Phone: +61 2 5550 1847
Web address: www.kestrelpointtours.com
Side 2
Taking pictures?
A Friendwall and Pixlane logo
Tag us in your pictures with
#kpwildtours
@kpwildtours
www.kestrelpointtours.com
Details:
Side 1
Logo
Name: Colin Warbeck
Role: Director
Phone: +61 2 5550 1847
Side 2
Taking pictures?
#kpwildtours
@kpwildtours

```html
<!DOCTYPE html>
<html lang="en">
<head>
<meta charset="utf-8">
<title>Kestrel Point Wildland Tours – Business Card</title>
<link rel="stylesheet" href="https://fonts.googleapis.com/css2?family=Montserrat:wght@500;700&family=Arimo:wght@400&display=swap">
<style>
  :root {
    --backdrop: #1c1c1e;
    --card-black: #111113;
    --card-grey: #2a2a2c;
    --paper: #ffffff;
    --amber: #f5a623;
    --amber-deep: #e8901a;
    --ink-light: #f2f2f2;
    --ink-dark: #2b2b2d;
  }
  * { box-sizing: border-box; margin: 0; padding: 0; }
  html, body { width: 1200px; height: 890px; overflow: hidden; }
  body {
    background: var(--backdrop);
    font-family: "Arimo", Arial, sans-serif;
    position: relative;
  }
  .card {
    position: absolute;
    top: 125px;
    width: 420px;
    height: 640px;
    border-radius: 26px;
    overflow: hidden;
    background: var(--card-black);
    box-shadow: 0 20px 40px rgba(0,0,0,.55);
  }
  .card--back { left: 150px; }
  .card--front {
    left: 630px;
    background: linear-gradient(160deg, var(--card-grey) 0%, var(--card-black) 55%);
  }

  /* brand lockup */
  .brand {
    position: absolute;
    left: 0; right: 0;
    display: flex;
    flex-direction: column;
    align-items: center;
    gap: 16px;
  }
  .brand__dot {
    width: 120px; height: 120px;
    border-radius: 50%;
    background: var(--amber);
  }
  .brand__name {
    font-family: "Montserrat", Arial, sans-serif;
    font-weight: 700;
    font-size: 17px;
    letter-spacing: 2px;
    text-transform: uppercase;
    text-align: center;
    line-height: 1.35;
  }
  .card--back .brand { top: 70px; }
  .card--back .brand__name { color: var(--ink-light); }
  .card--front .brand { top: 36px; z-index: 2; }
  .card--front .brand__name { color: var(--ink-dark); }

  /* back: social */
  .social {
    position: absolute;
    left: 0; right: 0; top: 420px;
    text-align: center;
    color: var(--ink-light);
  }
  .social__networks {
    display: flex; justify-content: center; gap: 18px;
    margin-bottom: 14px;
  }
  .social__network {
    font-family: "Montserrat", Arial, sans-serif;
    font-weight: 700;
    font-size: 14px;
    color: var(--amber);
  }
  .social__handle { font-size: 19px; line-height: 1.2; }

  /* front */
  .front-header { position: absolute; left: 0; top: 0; width: 420px; height: 330px; }
  .identity {
    position: absolute; left: 0; right: 0; top: 345px;
    text-align: center;
  }
  .identity__name {
    font-family: "Montserrat", Arial, sans-serif;
    font-weight: 500;
    font-size: 33px;
    letter-spacing: 1px;
    color: var(--amber);
  }
  .identity__role {
    font-family: "Montserrat", Arial, sans-serif;
    font-weight: 700;
    font-size: 21px;
    color: var(--ink-light);
    margin-top: 2px;
  }
  .icon-rule { position: absolute; left: 40px; top: 432px; width: 340px; height: 36px; }
  .contact {
    position: absolute; left: 0; right: 0; top: 478px;
    text-align: center;
    color: var(--ink-light);
    font-size: 19px;
    line-height: 1.25;
  }
  .divider {
    width: 240px; height: 2px; margin: 12px auto;
    background: linear-gradient(90deg, transparent, var(--amber), transparent);
  }
</style>
</head>
<body>

  <section class="card card--back" aria-label="Card reverse">
    <div class="brand">
      <div class="brand__dot"></div>
      <p class="brand__name">Kestrel Point<br>Wildland Tours</p>
    </div>
    <div class="social">
      <div class="social__networks">
        <span class="social__network">Pixlane</span>
        <span class="social__network">Friendwall</span>
      </div>
      <p class="social__handle">#kpwildtours</p>
      <p class="social__handle">@kpwildtours</p>
    </div>
  </section>

  <section class="card card--front" aria-label="Card front">
    <svg class="front-header" viewBox="0 0 420 330" aria-hidden="true">
      <path d="M0 0 H420 V250 Q210 345 0 250 Z" fill="var(--amber)"/>
      <path d="M0 0 H420 V236 Q210 330 0 236 Z" fill="var(--paper)"/>
    </svg>
    <div class="brand">
      <div class="brand__dot"></div>
      <p class="brand__name">Kestrel Point<br>Wildland Tours</p>
    </div>

    <div class="identity">
      <h1 class="identity__name">COLIN WARBECK</h1>
      <p class="identity__role">Director</p>
    </div>

    <svg class="icon-rule" viewBox="0 0 340 36" aria-hidden="true" fill="none" stroke="var(--amber)" stroke-width="2">
      <line x1="0" y1="18" x2="340" y2="18"/>
      <g fill="var(--card-black)">
        <circle cx="110" cy="18" r="15"/><circle cx="150" cy="18" r="15"/>
        <circle cx="190" cy="18" r="15"/><circle cx="230" cy="18" r="15"/>
      </g>
      <path d="M103 20 L110 12 L117 20 M105 19 V25 H115 V19"/>
      <path d="M145 11 Q141 18 145 25 L149 23 L147 19 L145 18 L147 15 Z" fill="var(--amber)" stroke="none"/>
      <rect x="182" y="13" width="16" height="11"/><path d="M182 13 L190 20 L198 13"/>
      <circle cx="230" cy="18" r="8"/><path d="M222 18 H238 M230 10 Q225 18 230 26 Q235 18 230 10"/>
    </svg>

    <div class="contact">
      <p>+61 2 5550 1847</p>
      <p>info@kestrelpointtours.com</p>
      <p>www.kestrelpointtours.com</p>
      <div class="divider"></div>
      <p>PO Box 71, Marlin Cove</p>
      <p>NSW 2471</p>
    </div>
  </section>

</body>
</html>
```